Trade fair QRVLN business card 7” x 5”

QRVLN exhibits on technology-hospitality trade fair in the UK this year. Therefore we are looking for well-designed marketing card (examples are linked in the bottom). The main role of these materials is to attract receivers to visit our website & find out more about QRVLN solutions.
Preferred used colours: white, various blue tints, black.
The front should contain branding & motto (“Modern beverage stocktaking”). Logotypes are attached.
The back should contain:
(value proposition),
Modern technology solution for beverage stocktaking
Accurate & effective stocktaking
Swift measuring with 99% accuracy makes stocktaking significantly quicker and more cost effective (or cost optimising).
Software solution supported with/by hardware tools
QRVLN system is based on universally accessible platforms - smartphones, PCs, and laptops. Your main measuring tool, smart scale, is delivered by QRVLN.
Smart & simple reporting system
Data availability - everywhere, anytime
Useful functions help stock managing at your bar
(call to action),
Find us on qrvln-example.com and try QRVLN with a one-month free trial.
(promo code)
Claim your 50% off discount with above promo code
Marketing card examples:
https://www.plinvoro-example.com/Which-startup-has-the-best-brochure-in-terms-of-design-and-content
Target Market(s)
QRVLN solution was created to help bar owners, bar managers and head bartenders to make their stocktaking process swift & accurate. Therefore, our product is targeting every business which sells portioned beverages.
Industry/Entity Type
Information Technology
Font styles to use
Look and feel
Each slider illustrates characteristics of the customer's brand and the style your logo design should communicate.

```html
<!DOCTYPE html>
<html lang="en">
<head>
<meta charset="utf-8">
<title>QRVLN Trade Fair Card</title>
<link href="https://fonts.googleapis.com/css2?family=Open+Sans:ital,wght@0,400;0,600;0,700;1,700;1,800&display=swap" rel="stylesheet">
<style>
  :root {
    --backdrop: #d9d9d9;
    --ink-white: #ffffff;
    --brand-blue: #2b7fc8;
    --accent-blue: #4ba3e3;
    --card-dark: #1d1c1c;
    --photo-warm-1: #3a2a20;
    --photo-warm-2: #6b4a33;
    --photo-warm-3: #a7774e;
    --placeholder-grey: #b5b5b5;
    --body-text: #f2f2f2;
  }
  * { margin: 0; padding: 0; box-sizing: border-box; }
  html, body { width: 885px; height: 1200px; overflow: hidden; }
  body {
    background: var(--backdrop);
    font-family: "Open Sans", Arial, sans-serif;
    position: relative;
  }
  .card {
    position: absolute;
    left: 90px;
    width: 700px;
    height: 500px;
    overflow: hidden;
    box-shadow: 0 6px 14px rgba(0,0,0,0.35);
  }
  .card--front { top: 78px; }
  .card--back { top: 638px; background: var(--card-dark); }

  /* Front */
  .front-photo {
    position: absolute; inset: 0;
    background:
      radial-gradient(ellipse at 40% 35%, rgba(150,90,70,0.55), transparent 55%),
      linear-gradient(100deg, var(--photo-warm-1) 0%, var(--photo-warm-2) 45%, var(--photo-warm-3) 75%, var(--photo-warm-1) 100%);
  }
  .front-photo::after {
    content: ""; position: absolute; inset: 0;
    background: rgba(0,0,0,0.28);
  }
  .brand-name {
    position: absolute; left: 0; right: 0;
    text-align: center;
    color: var(--ink-white);
    font-weight: 700;
    letter-spacing: 2px;
  }
  .card--front .brand-name { top: 266px; font-size: 74px; line-height: 1; }
  .brand-mark {
    display: inline-block;
    width: 0.62em; height: 0.62em;
    background: var(--ink-white);
    margin-right: 0.18em;
    vertical-align: 0.02em;
  }
  .motto {
    position: absolute; left: 0; right: 0; top: 378px;
    text-align: center;
    color: var(--ink-white);
    font-size: 16px; font-weight: 600;
    letter-spacing: 4.2px;
  }
  .web-band {
    position: absolute; left: 0; right: 0; top: 427px; height: 40px;
    background: var(--brand-blue);
    opacity: 0.92;
    display: flex; align-items: center; justify-content: center;
    color: var(--ink-white);
    font-size: 13px; letter-spacing: 2px;
  }

  /* Back */
  .back-photo {
    position: absolute; inset: 0;
    background:
      radial-gradient(ellipse at 50% 30%, rgba(80,60,50,0.35), transparent 60%),
      linear-gradient(180deg, #262322 0%, #1d1b1b 60%, #1a1a1a 100%);
  }
  .back-content { position: absolute; inset: 0; color: var(--ink-white); }
  .card--back .brand-name { top: 44px; font-size: 44px; line-height: 1; }
  .card--back .brand-mark { background: var(--accent-blue); }
  .back-title {
    position: absolute; left: 0; right: 0; top: 110px;
    text-align: center;
    font-size: 15px; letter-spacing: 1.3px;
  }
  .feature {
    position: absolute;
    display: flex; gap: 10px;
  }
  .feature-icon { width: 20px; height: 20px; flex: none; margin-top: 2px; }
  .feature-title {
    color: var(--accent-blue);
    font-size: 15px; line-height: 20px;
  }
  .feature-text {
    margin-top: 9px;
    font-size: 11.5px; line-height: 16px;
    text-align: justify;
    color: var(--body-text);
  }
  .f-accurate { left: 30px; top: 154px; width: 300px; }
  .f-reporting { left: 30px; top: 250px; width: 300px; }
  .f-data { left: 30px; top: 290px; width: 320px; }
  .f-software { left: 372px; top: 154px; width: 290px; }
  .f-functions { left: 372px; top: 294px; width: 290px; }

  .cta-band {
    position: absolute; left: 0; right: 0; top: 352px; height: 46px;
    background: var(--brand-blue);
    display: flex; align-items: center; justify-content: center;
    font-size: 18.5px; color: var(--ink-white);
  }
  .cta-band em { font-weight: 700; font-style: italic; margin: 0 5px; }
  .promo-box {
    position: absolute; left: 34px; top: 429px; width: 290px; height: 37px;
    background: var(--ink-white);
    display: flex; align-items: center; justify-content: center;
    color: var(--placeholder-grey); font-size: 12px;
  }
  .promo-claim {
    position: absolute; left: 375px; top: 428px;
    font-size: 12.5px; line-height: 1.2;
  }
  .promo-claim strong {
    font-size: 22px; font-weight: 800; font-style: italic;
  }
</style>
</head>
<body>

<section class="card card--front">
  <div class="front-photo" role="img" aria-label="Photo of a smiling bartender in a plaid shirt and apron standing at a warm-lit bar"></div>
  <div class="brand-name"><span class="brand-mark"></span>QRVLN</div>
  <div class="motto">MODERN BEVERAGE STOCKTAKING</div>
  <div class="web-band">www.qrvln-example.com</div>
</section>

<section class="card card--back">
  <div class="back-photo" role="img" aria-label="Dim, dark photo of a bar interior"></div>
  <div class="back-content">
    <div class="brand-name"><span class="brand-mark"></span>QRVLN</div>
    <div class="back-title">MODERN TECHNOLOGY SOLUTION FOR BEVERAGE STOCKTAKING</div>

    <div class="feature f-accurate">
      <svg class="feature-icon" viewBox="0 0 20 20" fill="#4ba3e3"><rect x="2" y="13" width="3" height="5"/><rect x="7" y="10" width="3" height="8"/><rect x="12" y="7" width="3" height="11"/><path d="M2 9 L9 4 L12 6 L17 2" stroke="#4ba3e3" stroke-width="1.6" fill="none"/><path d="M14 2 H18 V6 Z"/></svg>
      <div>
        <div class="feature-title">Accurate &amp; effective stocktaking</div>
        <p class="feature-text">Swift measuring with 99% accuracy makes stocktaking significantly quicker and more cost-effective</p>
      </div>
    </div>

    <div class="feature f-reporting">
      <svg class="feature-icon" viewBox="0 0 20 20" fill="#4ba3e3"><circle cx="10" cy="8" r="6"/><rect x="7" y="14" width="6" height="2"/><rect x="8" y="17" width="4" height="2"/></svg>
      <div class="feature-title">Smart &amp; simple reporting system</div>
    </div>

    <div class="feature f-data">
      <svg class="feature-icon" viewBox="0 0 20 20" fill="#4ba3e3"><rect x="1" y="3" width="12" height="9" rx="1"/><rect x="12" y="8" width="7" height="10" rx="1" stroke="#1d1c1c" stroke-width="1"/><rect x="4" y="13" width="7" height="2"/></svg>
      <div class="feature-title">Data availability - everywhere, anytime</div>
    </div>

    <div class="feature f-software">
      <svg class="feature-icon" viewBox="0 0 20 20" fill="none" stroke="#4ba3e3" stroke-width="2.4"><circle cx="7" cy="7" r="3.5" stroke-dasharray="2.2 1.4"/><circle cx="14" cy="14" r="3" stroke-dasharray="2 1.3"/></svg>
      <div>
        <div class="feature-title">Software solution supported by hardware tools</div>
        <p class="feature-text">QRVLN system is based on universally accessible platforms - smartphones, PCs, and laptops. Your main measuring tool, smart scale, is delivered by QRVLN.</p>
      </div>
    </div>

    <div class="feature f-functions">
      <svg class="feature-icon" viewBox="0 0 20 20" fill="#4ba3e3"><rect x="7" y="1" width="6" height="5"/><rect x="1" y="14" width="5" height="5"/><rect x="7.5" y="14" width="5" height="5"/><rect x="14" y="14" width="5" height="5"/><path d="M10 6 V14 M3.5 14 V10 H16.5 V14" stroke="#4ba3e3" stroke-width="1.4" fill="none"/></svg>
      <div class="feature-title">Useful functions help stock managing at your bar</div>
    </div>

    <div class="cta-band">Find us on qrvln-example.com and try <em>QRVLN</em> with a one-month free trial.</div>

    <div class="promo-box">(promo code)</div>
    <div class="promo-claim">Claim your<br><strong>50% off</strong> discount with promo code</div>
  </div>
</section>

</body>
</html>
```